Lumara Health & Wellness Business Card Design

We would like to create business cards matching with our new logo design. The card should be professional looking but still have a playful side and something that would be eye catching. We are planing to open a luxury medical spa and looking to create a design based on this new logo. We are looking for a design that shows off luxury but not be gold in color. Also, while we are a more female oriented medical center we do have men that come in for our services and it should be be too feminine.

Target Market(s)

Health & Wellness. Medical patients. Luxury spa

Industry/Entity Type

Health And Wellness

Contact Information for Business Card

It should have the logo design in the front of card and back of card should have our contact information. Our current colors are peach/ coral, teal, and gray. We are looking for a modern looking design.

Font styles to use
Script

Colors
32a6d6
e667a6
86cfc6
fece3e

Requirements
Must have
• It should have our logo design. We would prefer to have a more modern look to the card.
Nice to have
• Eye-Catching Design on the personable side but still classy.
Should not have
• At this point we are looking for the best design. It should not have color purple.

```html
<!DOCTYPE html>
<html lang="en">
<head>
<meta charset="utf-8">
<title>Lumara Health &amp; Wellness – Business Card</title>
<link rel="stylesheet" href="https://fonts.googleapis.com/css2?family=Montserrat:wght@400;500;600&display=swap">
<style>
  :root {
    --backdrop: #3a2f2a;
    --card-dark: #050505;
    --card-light: #ffffff;
    --ink-light: #ffffff;
    --ink-dark: #111111;
    --ink-soft: #333333;
  }
  * { box-sizing: border-box; margin: 0; padding: 0; }
  html, body {
    width: 1200px;
    height: 831px;
    overflow: hidden;
    background: var(--backdrop);
    font-family: "Montserrat", sans-serif;
  }
  .canvas {
    position: relative;
    width: 1200px;
    height: 831px;
  }
  .card {
    position: absolute;
    width: 560px;
    height: 320px;
    border-radius: 3px;
    box-shadow: 0 16px 34px rgba(0,0,0,.5);
  }
  .card--front {
    left: 40px;
    top: 80px;
    background: var(--card-dark);
    display: flex;
    align-items: center;
    justify-content: center;
  }
  .card--back {
    left: 600px;
    top: 440px;
    background: var(--card-light);
    display: flex;
    align-items: center;
    padding: 0 22px 0 34px;
  }
  .brand {
    display: flex;
    flex-direction: column;
    align-items: flex-start;
    font-weight: 500;
    line-height: 1;
  }
  .brand__name { letter-spacing: .06em; }
  .brand__line {
    text-transform: uppercase;
    letter-spacing: .16em;
    margin-top: 10px;
  }
  .card--front .brand { color: var(--ink-light); }
  .card--front .brand__name { font-size: 60px; }
  .card--front .brand__line { font-size: 17px; }
  .card--back .brand { color: var(--ink-dark); width: 200px; }
  .card--back .brand__name { font-size: 42px; }
  .card--back .brand__line { font-size: 12px; letter-spacing: .1em; margin-top: 8px; }
  .divider {
    width: 2px;
    height: 145px;
    background: var(--ink-dark);
    margin: 0 18px 0 16px;
    flex: none;
  }
  .contact { color: var(--ink-dark); }
  .contact__name { font-size: 23px; font-weight: 600; line-height: 1.15; }
  .contact__title { font-size: 16px; color: var(--ink-soft); margin-bottom: 12px; }
  .contact__list { list-style: none; font-size: 16px; line-height: 1.45; }
  .contact__list li { display: flex; align-items: center; gap: 8px; white-space: nowrap; }
  .contact__icon { width: 14px; height: 14px; flex: none; fill: var(--ink-dark); }
</style>
</head>
<body>
<main class="canvas">
  <section class="card card--front" aria-label="Card front">
    <div class="brand">
      <span class="brand__name">Lumara</span>
      <span class="brand__line">Health &amp; Wellness</span>
    </div>
  </section>

  <section class="card card--back" aria-label="Card back">
    <div class="brand">
      <span class="brand__name">Lumara</span>
      <span class="brand__line">Health &amp; Wellness</span>
    </div>
    <div class="divider"></div>
    <div class="contact">
      <p class="contact__name">Your Name</p>
      <p class="contact__title">Your Title</p>
      <ul class="contact__list">
        <li>
          <svg class="contact__icon" viewBox="0 0 16 16" aria-hidden="true"><path d="M3.2 1l2.6 2.6-1.4 2.2c.9 1.9 2.3 3.3 4.2 4.2l2.2-1.4L15 11.2 13.3 14C7 14 2 9 2 2.7z"/></svg>
          123-456-2100
        </li>
        <li>
          <svg class="contact__icon" viewBox="0 0 16 16" aria-hidden="true"><path d="M1 3h14v10H1z M2 4l6 5 6-5" fill="none" stroke="#111" stroke-width="1.6"/></svg>
          youremail@lumaramail.com
        </li>
        <li>
          <svg class="contact__icon" viewBox="0 0 16 16" aria-hidden="true"><circle cx="8" cy="8" r="6.5" fill="none" stroke="#111" stroke-width="1.5"/><path d="M1.5 8h13M8 1.5c-3 3.5-3 9.5 0 13M8 1.5c3 3.5 3 9.5 0 13" fill="none" stroke="#111" stroke-width="1.2"/></svg>
          www.yourwebsite.com
        </li>
      </ul>
    </div>
  </section>
</main>
</body>
</html>
```